Silver Creek Plumbing Business card & letter head design

We need a new business card and letter head for our plumbing company called silver creek plumbing. attached is the companys logo. We provide domestic and commercial plumbing services in regional western Australia. We are after Something simple yet nice to look at and something that fits within the trade industry.

Target Market(s)

trade/building industry

Contact Information for Business Card

Darl Hensby
Manager
0461 238 574
enquiries@scplumbwork.net.au
ABN: 47 381 905 462
PCL: 5187

Domestic & Commercial Plumbing
Tip Truck & Excavator hire

Colors

Designer to choose colors to be used in the design.

```html
<!DOCTYPE html>
<html lang="en">
<head>
<meta charset="utf-8">
<title>Silver Creek Plumbing – Stationery</title>
<link rel="stylesheet" href="https://fonts.googleapis.com/css2?family=Questrial&family=Lato:wght@400&family=Libre+Baskerville:wght@700&family=Great+Vibes&display=swap">
<style>
  :root {
    --brand-blue: #1557a6;
    --ink: #4a4a4a;
    --ink-soft: #6b6b6b;
    --paper: #ffffff;
    --backdrop: #dddddd;
    --rule: #8a8a8a;
  }
  * { box-sizing: border-box; margin: 0; padding: 0; }
  html, body { width: 1200px; height: 1017px; overflow: hidden; }
  body {
    position: relative;
    background: var(--backdrop);
    font-family: "Questrial", sans-serif;
    color: var(--ink);
  }
  .abs { position: absolute; }

  /* Brand wordmark */
  .wordmark { text-align: center; line-height: 1; }
  .wordmark .wm-main { display: block; letter-spacing: -0.5px; }
  .wordmark .wm-sub { display: block; letter-spacing: 0.42em; margin-right: -0.42em; }

  /* Card front */
  .card-front {
    left: 78px; top: 202px; width: 501px; height: 285px;
    background: var(--brand-blue); color: var(--paper);
  }
  .card-front .wordmark { left: 0; right: 0; top: 112px; color: var(--paper); }
  .card-front .wm-main { font-size: 31px; }
  .card-front .wm-sub { font-size: 15px; margin-top: 8px; }
  .card-front .services {
    left: 0; right: 0; top: 222px; text-align: center;
    font-size: 12.6px; line-height: 20.5px; letter-spacing: 0.2px;
  }

  /* Card back */
  .card-back {
    left: 78px; top: 535px; width: 501px; height: 285px;
    background: var(--paper);
  }
  .card-back .band { left: 0; right: 0; bottom: 0; height: 8px; background: var(--brand-blue); }
  .card-back .edge-tab {
    left: 493px; top: 48px; width: 8px; height: 37px;
    background: var(--brand-blue); border-radius: 7px 0 0 7px;
  }
  .card-back .wordmark { left: 30px; width: 176px; top: 45px; color: var(--brand-blue); }
  .card-back .wm-main { font-size: 23px; }
  .card-back .wm-sub { font-size: 11.5px; margin-top: 6px; }
  .card-back .holder { right: 31px; top: 44px; text-align: right; }
  .card-back .holder-name {
    font-family: "Libre Baskerville", serif; font-weight: 700;
    font-size: 19px; color: var(--brand-blue); letter-spacing: 0.3px;
  }
  .card-back .holder-role { font-size: 15px; color: var(--ink-soft); margin-top: 3px; }
  .card-back .registration {
    right: 31px; top: 132px; text-align: right; font-size: 12.8px; line-height: 17.5px;
  }
  .card-back .divider { left: 31px; right: 31px; top: 182px; height: 1px; background: var(--rule); }
  .contact-list { list-style: none; }
  .card-back .contact-list { left: 31px; top: 200px; font-size: 12.8px; line-height: 20.5px; }
  .contact-list li { display: flex; align-items: center; gap: 6px; white-space: nowrap; }
  .contact-list svg { flex: none; fill: var(--brand-blue); }
  .card-back .services {
    right: 31px; top: 223px; text-align: right; font-size: 12.8px; line-height: 18px; letter-spacing: 0.2px;
  }

  /* Letterhead */
  .letterhead {
    left: 646px; top: 167px; width: 484px; height: 683px;
    background: var(--paper);
  }
  .letterhead .band { left: 0; right: 0; bottom: 0; height: 8px; background: var(--brand-blue); }
  .letterhead .wordmark { left: 23px; width: 162px; top: 62px; color: var(--brand-blue); }
  .letterhead .wm-main { font-size: 21px; }
  .letterhead .wm-sub { font-size: 10px; margin-top: 5px; }
  .letterhead .sender-rule { left: 317px; top: 32px; width: 2px; height: 70px; background: var(--brand-blue); }
  .letterhead .sender { left: 332px; top: 30px; font-size: 7px; line-height: 10.2px; color: var(--ink); }
  .letterhead .sender-name { font-size: 10.5px; color: var(--brand-blue); line-height: 13px; }
  .letterhead .sender-role { font-size: 8px; line-height: 11px; }
  .letterhead .sender .contact-list li { gap: 3px; }
  .letterhead .recipient {
    left: 24px; top: 190px; font-family: "Lato", sans-serif; font-size: 7px; line-height: 10.7px; color: var(--ink-soft);
  }
  .letterhead .salutation { left: 24px; top: 258px; font-family: "Lato", sans-serif; font-size: 9.5px; color: var(--ink-soft); }
  .letterhead .letter-body {
    left: 24px; top: 287px; width: 436px;
    font-family: "Lato", sans-serif; font-size: 6.4px; line-height: 10.7px; color: var(--ink-soft);
  }
  .letter-body p { text-align: justify; margin-bottom: 13.2px; }
  .letterhead .sign-off { left: 24px; top: 512px; font-family: "Lato", sans-serif; font-size: 8.3px; color: var(--ink-soft); }
  .letterhead .signature { left: 24px; top: 530px; font-family: "Great Vibes", cursive; font-size: 14px; color: var(--brand-blue); }
  .letterhead .footer-rule { left: 131px; width: 225px; top: 648px; height: 1px; background: var(--brand-blue); }
  .letterhead .footer-text { left: 131px; top: 654px; font-size: 7.6px; color: var(--ink); white-space: nowrap; }
</style>
</head>
<body>

<!-- Business card: front -->
<section class="abs card-front" aria-label="Business card front">
  <div class="abs wordmark">
    <span class="wm-main">SILVER CREEK</span>
    <span class="wm-sub">PLUMBING</span>
  </div>
  <p class="abs services">Domestic &amp; Commercial Plumbing<br>Tip Truck &amp; Excavator hire</p>
</section>

<!-- Business card: back -->
<section class="abs card-back" aria-label="Business card back">
  <div class="abs edge-tab"></div>
  <div class="abs wordmark">
    <span class="wm-main">SILVER CREEK</span>
    <span class="wm-sub">PLUMBING</span>
  </div>
  <div class="abs holder">
    <p class="holder-name">DARL HENSBY</p>
    <p class="holder-role">Manager</p>
  </div>
  <p class="abs registration">ABN: 47 381 905 462<br>PCL: 5187</p>
  <div class="abs divider"></div>
  <ul class="abs contact-list">
    <li><svg width="8" height="11" viewBox="0 0 8 11"><path d="M1.5 0h5A1.5 1.5 0 0 1 8 1.5v8A1.5 1.5 0 0 1 6.5 11h-5A1.5 1.5 0 0 1 0 9.5v-8A1.5 1.5 0 0 1 1.5 0zM1.3 1.4v6.8h5.4V1.4zM4 8.8a.8.8 0 1 0 0 1.6.8.8 0 0 0 0-1.6z"/></svg>0461 238 574</li>
    <li><svg width="9" height="7" viewBox="0 0 9 7"><path d="M0 0h9v7H0zM1 1.2v4.8h7V1.2L4.5 3.8z"/></svg>enquiries@scplumbwork.net.au</li>
    <li><svg width="9" height="9" viewBox="0 0 10 10"><circle cx="5" cy="5" r="5"/><path d="M2.2 3.2c1 .2 1.6 1 1.3 2-.3.8.6 1.4.8 2.4M6.2 1.1c-.4.9.5 1.5 1.4 1.7.8.2.6 1.2 1.5 1.4" stroke="#fff" stroke-width="1" fill="none"/></svg>www.scplumbwork.net.au</li>
  </ul>
  <p class="abs services">Domestic &amp; Commercial Plumbing<br>Tip Truck &amp; Excavator hire</p>
  <div class="abs band"></div>
</section>

<!-- Letterhead -->
<section class="abs letterhead" aria-label="Letterhead">
  <div class="abs wordmark">
    <span class="wm-main">SILVER CREEK</span>
    <span class="wm-sub">PLUMBING</span>
  </div>
  <div class="abs sender-rule"></div>
  <div class="abs sender">
    <p class="sender-name">DARL HENSBY</p>
    <p class="sender-role">Manager</p>
    <p>ABN: 47 381 905 462</p>
    <p>PCL: 5187</p>
    <ul class="contact-list">
      <li><svg width="5" height="7" viewBox="0 0 8 11"><path d="M1.5 0h5A1.5 1.5 0 0 1 8 1.5v8A1.5 1.5 0 0 1 6.5 11h-5A1.5 1.5 0 0 1 0 9.5v-8A1.5 1.5 0 0 1 1.5 0zM1.3 1.4v6.8h5.4V1.4zM4 8.8a.8.8 0 1 0 0 1.6.8.8 0 0 0 0-1.6z"/></svg>0461 238 574</li>
      <li><svg width="6" height="5" viewBox="0 0 9 7"><path d="M0 0h9v7H0zM1 1.2v4.8h7V1.2L4.5 3.8z"/></svg>enquiries@scplumbwork.net.au</li>
      <li><svg width="6" height="6" viewBox="0 0 10 10"><circle cx="5" cy="5" r="5"/><path d="M2.2 3.2c1 .2 1.6 1 1.3 2-.3.8.6 1.4.8 2.4M6.2 1.1c-.4.9.5 1.5 1.4 1.7.8.2.6 1.2 1.5 1.4" stroke="#fff" stroke-width="1" fill="none"/></svg>www.scplumbwork.net.au</li>
    </ul>
  </div>

  <address class="abs recipient" style="font-style:normal">
    Mr/s<br>First Name and Last Name<br>Company Name<br>Address
  </address>
  <p class="abs salutation">Dear Sir</p>

  <div class="abs letter-body">
    <p>This sample paragraph stands in for the body of the letter and shows how the text block sits on the page. It runs across the full width of the sheet with even spacing between lines, so the reader can follow each line easily. Replace this copy with the real message before the letter goes out to a client or supplier in the region. Each section keeps the same left margin as the address block above, and the closing line and signature follow after the final paragraph near the lower part of the sheet.</p>
    <p>This sample paragraph stands in for the body of the letter and shows how the text block sits on the page. It runs across the full width of the sheet with even spacing between lines, so the reader can follow each line easily. Replace this copy with the real message before the letter goes out to a client or supplier in the region. Each section keeps the same left margin as the address block above, and the closing line and signature follow after the final paragraph near the lower part of the sheet.</p>
    <p>This sample paragraph stands in for the body of the letter and shows how the text block sits on the page. It runs across the full width of the sheet with even spacing between lines, so the reader can follow each line easily. Replace this copy with the real message before the letter goes out to a client or supplier in the region. Each section keeps the same left margin as the address block above, and the closing line and signature follow after the final paragraph near the lower part of the sheet.</p>
    <p>This sample paragraph stands in for the body of the letter and shows how the text block sits on the page. It runs across the full width of the sheet with even spacing between lines, so the reader can follow each line easily. Replace this copy with the real message before the letter goes out to a client or supplier in the region. Each section keeps the same left margin as the address block above, and the closing line and signature follow after the final paragraph near the lower part of the sheet.</p>
  </div>

  <p class="abs sign-off">Harbour Ledger Group LTD</p>
  <p class="abs signature">Marla Tennick</p>

  <div class="abs footer-rule"></div>
  <p class="abs footer-text">Domestic &amp; Commercial Plumbing Tip Truck &amp; Excavator hire</p>
  <div class="abs band"></div>
</section>

</body>
</html>
```